Marlow Cybersecurity Secives professional web site

Marlow is a unit of the Tesselcore company, based on the audit services it offers and which mainly works by the contacts it has from its previous experience. The objective with the development of this website will be to increase its presence on the internet and even link the traffic of its social networks with the blog of the new page and in this way, provide information for old and potential customers.
For this reason, we will set the objective of the page, have all the information of the company, its services and its scope in general, in a formal and simple for users, facilitating the task of finding the information they want within of the page, as well as, including the option of feedback.

Target Market(s)

any company that needs security assessments

Number of Pages Required

4 page

Font styles to use
Sans Serif

Colors

Designer to choose colors to be used in the design.

Requirements
Must have
• READ THE PDF PLEASE. Video in homepage, cool graphics, color like our logo
• I like the following sites: www.tesselcore-example.com & www.quarbitex-example.com
Nice to have
• Futuristic
Should not have
• Please, dont use the gallery pictures I used in my document, I prefer hand made illustrations instead

```html
<!DOCTYPE html>
<html lang="en">
<head>
<meta charset="utf-8">
<title>Marlow Security – Leading Digital Performance Agency</title>
<link href="https://fonts.googleapis.com/css2?family=Roboto:wght@300;400;500;700;900&display=swap" rel="stylesheet">
<style>
:root{
  --red:#c8202f;
  --red-deep:#a81825;
  --ink:#1f1f1f;
  --text:#6b6b6b;
  --muted:#9a9a9a;
  --light:#f5f5f5;
  --white:#ffffff;
  --navy:#0d2134;
  --navy-2:#1b3d5a;
  --admin:#23282d;
  --footer:#1c1e22;
  --footer-text:#8d9096;
  --container:675px;
}
*{box-sizing:border-box;margin:0;padding:0}
html,body{width:1200px;height:4203px;overflow:hidden}
body{font-family:"Roboto",Arial,sans-serif;color:var(--text);background:var(--white);font-size:12px;line-height:1.6}
.container{width:var(--container);margin:0 auto;position:relative}
.center{text-align:center}

/* admin bar */
.admin-bar{height:16px;background:var(--admin);color:#ccc;font-size:8px;line-height:16px;padding:0 10px;display:flex;gap:14px}
.admin-bar .howdy{margin-left:auto}

/* hero */
.hero{position:relative;height:539px;background:radial-gradient(ellipse at 60% 40%,#2c5a7e 0%,#153550 40%,#0a1a2a 100%);color:var(--white)}
.hero-bg{position:absolute;inset:0}
.topline{position:absolute;top:4px;left:262px;font-size:8px;color:#cfd8e0;display:flex;gap:14px}
.site-header{position:absolute;top:46px;left:262px;width:675px;display:flex;align-items:center;justify-content:space-between}
.brand{display:flex;align-items:center;gap:6px;font-weight:900;font-size:12px;line-height:1;color:var(--white);letter-spacing:.5px}
.brand-mark{width:28px;height:28px;border-radius:50%;background:var(--red)}
.main-nav{display:flex;gap:16px;font-size:9px;font-weight:700;letter-spacing:.3px}
.hero-content{position:absolute;top:230px;left:0;right:0;text-align:center}
.hero h1{font-size:36px;font-weight:700;line-height:1.2;letter-spacing:.5px}
.hero p{width:500px;margin:12px auto 0;font-size:10px;line-height:1.5;color:#dfe6ec}
.btn-red{display:inline-block;background:var(--red);color:var(--white);font-size:10px;font-weight:700;padding:7px 16px;letter-spacing:.4px}
.hero .btn-red{margin-top:18px}

/* shared section titles */
.eyebrow{color:var(--red);font-size:10px;letter-spacing:4px;font-weight:500}
.section-title{font-size:21px;font-weight:400;color:var(--ink);letter-spacing:.5px;text-transform:uppercase}
.section-title b{font-weight:700}
.rule{width:42px;height:2px;background:var(--red);margin:10px auto}
.lead{font-size:10px;color:var(--text);width:520px;margin:0 auto}

/* intro */
.intro{height:285px;padding-top:44px}
.intro h2{font-size:29px;font-weight:700;color:var(--ink);line-height:1.1;margin-top:6px}
.intro .lead{margin-top:14px}
.intro .rule{margin-top:18px}

/* about */
.about{height:264px}
.about .container{display:flex;gap:30px}
.about-text{width:324px}
.about-text h3{font-size:17px;font-weight:700;color:var(--ink);line-height:1.15;text-transform:uppercase}
.about-text p{font-size:10px;line-height:1.5;margin-top:10px}
.about-media{width:321px;height:216px;background:linear-gradient(135deg,#0c1d33 0%,#2a5b8c 50%,#cfe4f5 70%,#11263e 100%)}

/* services */
.services{height:591px;background:var(--light);padding-top:48px}
.services .lead{margin-top:4px}
.service-grid{display:grid;grid-template-columns:repeat(3,225px);row-gap:48px;margin-top:36px}
.service{text-align:center;padding:0 14px}
.service svg{width:22px;height:22px;stroke:var(--red);fill:none;stroke-width:1.8}
.service h4{font-size:10px;font-weight:700;color:var(--ink);margin-top:6px;text-transform:uppercase;line-height:1.3}
.service p{font-size:9px;line-height:1.45;margin-top:3px}
.learn{font-size:9px;color:var(--red);font-weight:500;margin-top:8px;display:block}

/* stats */
.stats{height:381px;position:relative;color:var(--white);background:linear-gradient(120deg,#c42a3e 0%,#d9485a 45%,#b8233a 100%)}
.stats .container{padding-top:78px;text-align:center}
.stats h2{font-size:20px;font-weight:400}
.stats .lead{color:#f6d6da;margin-top:10px}
.stat-row{display:flex;justify-content:space-between;width:560px;margin:104px auto 0}
.stat{width:180px;text-align:center}
.stat strong{display:block;font-size:38px;font-weight:700;line-height:1}
.stat span{display:block;font-size:9px;font-weight:700;margin-top:8px;text-transform:uppercase}

/* clients */
.clients{height:411px;padding-top:28px}
.clients .lead{margin-top:10px}
.client-grid{display:grid;grid-template-columns:repeat(4,1fr);width:560px;margin:58px auto 0;row-gap:100px}
.client{display:flex;align-items:center;justify-content:center;gap:6px;font-size:20px;font-weight:700;color:#5a5a5a}
.client i{width:14px;height:14px;border-radius:50%;background:#5a5a5a;display:inline-block}

/* testimonials */
.testimonials{height:330px;padding-top:0}
.testimonials .lead{margin-top:6px}
.testimonial-row{display:flex;justify-content:space-between;margin-top:56px}
.testimonial{position:relative;width:318px;height:117px;border:1px solid var(--red);display:flex;gap:12px;padding:24px 20px 0}
.quote-badge{position:absolute;top:-9px;left:150px;width:18px;height:18px;border-radius:50%;border:1px solid var(--red);background:var(--white)}
.avatar{width:44px;height:44px;border-radius:50%;flex:none;background:linear-gradient(135deg,#e9c8a8,#b98a63)}
.avatar.alt{background:linear-gradient(135deg,#9aa3ac,#4b5560)}
.testimonial p{font-size:9px;line-height:1.45;color:var(--text)}
.testimonial .who{font-size:8px;font-weight:700;color:var(--ink);margin-top:8px;text-transform:uppercase;line-height:1.4}

/* blog */
.blog{height:630px;background:var(--light);padding-top:124px}
.blog .lead{margin-top:6px}
.blog-grid{display:flex;justify-content:space-between;margin-top:56px}
.post{width:201px}
.post-media{height:120px}
.post-media.a{background:linear-gradient(135deg,#d7d2c8,#7d6a5a)}
.post-media.b{background:linear-gradient(135deg,#c8dde8,#3d6a88)}
.post-media.c{background:linear-gradient(135deg,#ddd3c4,#6f5f55)}
.post h4{font-size:14px;font-weight:700;color:var(--ink);line-height:1.12;margin-top:10px;text-transform:uppercase}
.post p{font-size:9px;line-height:1.45;margin-top:4px}
.btn-outline{display:inline-block;border:1px solid var(--red);color:var(--red);font-size:8px;font-weight:700;padding:5px 12px;margin-top:10px}
.blog .btn-red{margin-top:44px;font-size:9px;padding:6px 10px}

/* careers */
.careers{height:474px;background:var(--red);color:var(--white);text-align:center;padding-top:76px}
.careers h2{font-size:28px;font-weight:700;letter-spacing:3px}
.careers-brand{display:flex;align-items:center;justify-content:center;gap:14px;margin-top:18px}
.careers-brand .name{font-size:38px;font-weight:900;line-height:.95;text-align:right}
.careers-brand .mark{width:96px;height:96px;border-radius:50%;background:var(--white)}
.careers p{font-size:11px;font-weight:500;margin-top:26px}
.btn-ghost{display:inline-block;border:1px solid var(--white);color:var(--white);font-size:9px;font-weight:500;padding:6px 14px;margin-top:16px}

/* footer */
.site-footer{height:294px;background:var(--footer);color:var(--footer-text);padding-top:42px}
.footer-cols{display:flex}
.footer-col h5{font-size:10px;font-weight:700;color:var(--white);text-transform:uppercase;letter-spacing:.4px}
.about-col{width:240px}
.about-col p{font-size:8px;line-height:1.5;margin-top:10px;width:200px}
.links-col{width:234px}
.links-col ul{list-style:none;margin-top:10px;font-size:8px;line-height:1.75}
.news-col{width:201px}
.field{height:27px;background:var(--white);color:#999;font-size:8px;padding:0 8px;line-height:27px;margin-top:12px}
.news-col h5 + .field{margin-top:14px}
.subscribe{height:24px;background:var(--red);color:var(--white);font-size:9px;font-weight:700;letter-spacing:2px;text-align:center;line-height:24px;margin-top:12px}
.social{display:flex;gap:6px;margin-top:12px}
.social span{width:14px;height:14px;border-radius:50%;background:var(--red)}
.copyright{font-size:8px;margin-top:14px}
</style>
</head>
<body>

<div class="admin-bar">
  <span>My Site</span><span>Edit Page</span><span>Enable Visual Builder</span><span class="howdy">Howdy, admin</span>
</div>

<header class="hero">
  <div class="hero-bg" role="img" aria-label="Dark blue network visual with connected nodes and security icons behind a person at work"></div>
  <div class="topline"><span>+1 555 0142 7781</span><span>info@marlowsecurity-example.com</span></div>
  <div class="site-header">
    <div class="brand"><span>MARLOW<br>SECURITY</span><span class="brand-mark"></span></div>
    <nav class="main-nav"><span>HOME</span><span>ABOUT US</span><span>SERVICES</span><span>BLOG</span><span>CONTACT US</span></nav>
  </div>
  <div class="hero-content">
    <h1>LEADING DIGITAL<br>PERFORMANCE AGENCY</h1>
    <p>Lorem ipsum dolor sit amet, consectetur adipiscing elit, sed do eiusmod tempor incididunt ut labore et dolore magna aliqua. Ut enim ad minim veniam, quis nostrud exercitation ullamco.</p>
    <span class="btn-red">GET IN TOUCH</span>
  </div>
</header>

<section class="intro center">
  <div class="container">
    <div class="eyebrow">WE ARE</div>
    <h2>A RELIABLE DIGITAL<br>PERFORMANCE AGENCY</h2>
    <p class="lead">Lorem ipsum dolor sit amet, consectetur adipiscing elit, sed do eiusmod tempor incididunt ut labore et dolore magna aliqua. Ut enim ad minim veniam, quis nostrud exercitation ullamco laboris.</p>
    <div class="rule"></div>
  </div>
</section>

<section class="about">
  <div class="container">
    <div class="about-text">
      <h3>Connecting data to discover insights that drive business outcomes</h3>
      <p>Lorem ipsum dolor sit amet, consectetur adipiscing elit, sed do eiusmod tempor incididunt ut labore et dolore magna aliqua. Ut enim ad minim veniam, quis nostrud exercitation ullamco laboris nisi ut aliquip ex ea commodo consequat.</p>
      <p>Lorem ipsum dolor sit amet, consectetur adipiscing elit, sed do eiusmod tempor incididunt ut labore et dolore magna aliqua. Ut enim ad minim veniam, quis nostrud exercitation ullamco laboris nisi ut aliquip ex ea commodo consequat.</p>
    </div>
    <div class="about-media" role="img" aria-label="Hand holding a glowing network of connected points"></div>
  </div>
</section>

<section class="services">
  <div class="container center">
    <h2 class="section-title">OUR <b>SERVICES</b></h2>
    <div class="rule"></div>
    <p class="lead">Lorem ipsum dolor sit amet, consectetur adipiscing elit, sed do eiusmod tempor incididunt ut.</p>
    <div class="service-grid">
      <div class="service">
        <svg viewBox="0 0 24 24"><path d="M3 6l6-2 6 2 6-2v14l-6 2-6-2-6 2z"/><path d="M9 4v14M15 6v14"/></svg>
        <h4>Webpage Audit</h4>
        <p>Lorem ipsum dolor sit amet, consectetur adipiscing elit, sed do eiusmod tempor incididunt.</p>
        <span class="learn">Learn More</span>
      </div>
      <div class="service">
        <svg viewBox="0 0 24 24"><path d="M14 4a5 5 0 0 0 6 6l-10 10-4-4 10-10"/></svg>
        <h4>Internal and External Audit</h4>
        <p>Lorem ipsum dolor sit amet, consectetur adipiscing elit, sed do eiusmod tempor incididunt.</p>
        <span class="learn">Learn More</span>
      </div>
      <div class="service">
        <svg viewBox="0 0 24 24"><circle cx="12" cy="12" r="3.5"/><path d="M12 2v4M12 18v4M2 12h4M18 12h4M5 5l3 3M16 16l3 3M19 5l-3 3M8 16l-3 3"/></svg>
        <h4>Web Application Audit</h4>
        <p>Lorem ipsum dolor sit amet, consectetur adipiscing elit, sed do eiusmod tempor incididunt.</p>
        <span class="learn">Learn More</span>
      </div>
      <div class="service">
        <svg viewBox="0 0 24 24"><path d="M20 3L10 13M10 13c-3 0-5 2-5 4s-1 3-2 4c4 0 8-1 8-5"/></svg>
        <h4>Source Code Audit</h4>
        <p>Lorem ipsum dolor sit amet, consectetur adipiscing elit, sed do eiusmod tempor incididunt.</p>
        <span class="learn">Learn More</span>
      </div>
      <div class="service">
        <svg viewBox="0 0 24 24"><rect x="3" y="4" width="18" height="12" rx="1"/><path d="M8 20h8M12 16v4"/></svg>
        <h4>Digital Forensics &amp; Incident Response</h4>
        <p>Lorem ipsum dolor sit amet, consectetur adipiscing elit, sed do eiusmod tempor incididunt.</p>
        <span class="learn">Learn More</span>
      </div>
      <div class="service">
        <svg viewBox="0 0 24 24"><rect x="5" y="4" width="14" height="17" rx="1"/><path d="M9 4V2h6v2M8 11l3 3 5-5"/></svg>
        <h4>Report Resolution</h4>
        <p>Lorem ipsum dolor sit amet, consectetur adipiscing elit, sed do eiusmod tempor incididunt.</p>
        <span class="learn">Learn More</span>
      </div>
    </div>
  </div>
</section>

<section class="stats" role="img" aria-label="Team working at a table seen from above, tinted red">
  <div class="container">
    <h2>we are the best cyber security in town</h2>
    <p class="lead">Lorem ipsum dolor sit amet, consectetur adipiscing elit, sed do eiusmod tempor incididunt ut labore et dolore magna aliqua. Ut enim ad minim.</p>
    <div class="stat-row">
      <div class="stat"><strong>20%</strong><span>Increase in sales</span></div>
      <div class="stat"><strong>41%</strong><span>Happy clients</span></div>
      <div class="stat"><strong>26%</strong><span>Increase in conversions</span></div>
    </div>
  </div>
</section>

<section class="clients center">
  <div class="container">
    <h2 class="section-title">OUR <b>CLIENTS</b></h2>
    <div class="rule"></div>
    <p class="lead">Lorem ipsum dolor sit amet, consectetur adipiscing elit, sed do eiusmod tempor incididunt ut.</p>
    <div class="client-grid">
      <div class="client"><i></i>Ringwell</div>
      <div class="client">Skylark</div>
      <div class="client">Beacon</div>
      <div class="client">Harrow</div>
      <div class="client">Vantis</div>
      <div class="client"><i></i>Cardex</div>
      <div class="client">Millbrook</div>
      <div class="client">Norvo</div>
    </div>
  </div>
</section>

<section class="testimonials center">
  <div class="container">
    <h2 class="section-title">OUR <b>TESTIMONIALS</b></h2>
    <div class="rule"></div>
    <p class="lead">Lorem ipsum dolor sit amet, consectetur adipiscing elit, sed do eiusmod tempor incididunt ut.</p>
    <div class="testimonial-row">
      <div class="testimonial">
        <span class="quote-badge"></span>
        <div class="avatar" role="img" aria-label="Portrait of a client"></div>
        <div class="center" style="text-align:left">
          <p>I wanted to hire the best and after looking at several other companies, I knew Jacob was the perfect guy for the job. He is a true professional.</p>
          <div class="who">Dana Morrow<br>Graphic Designer</div>
        </div>
      </div>
      <div class="testimonial">
        <span class="quote-badge"></span>
        <div class="avatar alt" role="img" aria-label="Portrait of a client"></div>
        <div style="text-align:left">
          <p>I wanted to hire the best and after looking at several other companies, I knew Jacob was the perfect guy for the job. He is a true professional.</p>
          <div class="who">Dana Morrow<br>Graphic Designer</div>
        </div>
      </div>
    </div>
  </div>
</section>

<section class="blog">
  <div class="container center">
    <h2 class="section-title">OUR <b>BLOG</b></h2>
    <div class="rule"></div>
    <p class="lead">Lorem ipsum dolor sit amet, consectetur adipiscing elit, sed do eiusmod tempor incididunt ut.</p>
    <div class="blog-grid" style="text-align:left">
      <article class="post">
        <div class="post-media a" role="img" aria-label="Colleagues talking in an office"></div>
        <h4>We are Nova. A letter from our founders, Aran Holt and Lee Wren</h4>
        <p>Lorem ipsum dolor sit amet, consectetur adipiscing elit, sed do eiusmod tempor incididunt ut labore et dolore magna aliqua.</p>
        <span class="btn-outline">READ MORE</span>
      </article>
      <article class="post">
        <div class="post-media b" role="img" aria-label="Person working on a laptop"></div>
        <h4>So what is marketing intelligence and why should we care?</h4>
        <p>Lorem ipsum dolor sit amet, consectetur adipiscing elit, sed do eiusmod tempor incididunt ut labore et dolore magna aliqua.</p>
        <span class="btn-outline">READ MORE</span>
      </article>
      <article class="post">
        <div class="post-media c" role="img" aria-label="Team standing together"></div>
        <h4>So what is marketing intelligence and why should we care?</h4>
        <p>Lorem ipsum dolor sit amet, consectetur adipiscing elit, sed do eiusmod tempor incididunt ut labore et dolore magna aliqua.</p>
        <span class="btn-outline">READ MORE</span>
      </article>
    </div>
    <span class="btn-red">VIEW ALL BLOG ENTRIES</span>
  </div>
</section>

<section class="careers">
  <h2>WORK WITH</h2>
  <div class="careers-brand">
    <div class="name">MARLOW<br>SECURITY</div>
    <span class="mark"></span>
  </div>
  <p>We're always looking for talented people to join our team.</p>
  <span class="btn-ghost">OUR CURRENT VACANCIES</span>
</section>

<footer class="site-footer">
  <div class="container">
    <div class="footer-cols">
      <div class="footer-col about-col">
        <h5>About Us</h5>
        <p>Lorem ipsum dolor sit amet, consectetur adipiscing elit, sed do eiusmod tempor incididunt ut labore et dolore magna.</p>
        <p>Address: 14 Harbour Lane, Springfield<br>Email: info@marlowsecurity-example.com<br>Phone: +1 555 0142 7781</p>
        <div class="social"><span></span><span></span><span></span></div>
        <div class="copyright">Marlow security 2018. All rights reserved.</div>
      </div>
      <div class="footer-col links-col">
        <h5>Quick Links</h5>
        <ul><li>HOME</li><li>ABOUT US</li><li>SERVICES</li><li>BLOG</li><li>CONTACT US</li></ul>
      </div>
      <div class="footer-col news-col">
        <h5>Subscribe to Newsletter</h5>
        <div class="field">First Name</div>
        <div class="field">Last Name</div>
        <div class="field">Email</div>
        <div class="subscribe">SUBSCRIBE</div>
      </div>
    </div>
  </div>
</footer>

</body>
</html>
```